Corporate Identity Pack - LetterHead, Business Card, Envelope

We are looking for a clean, professional, and visually connected corporate identity set for our company "MERIDA CARE" (Cleaning, Gardening, and Pest Control services).

The pack must include:

Business Card (front and back)
Envelope with recipient window on the right side (22x11)
A4 Letterhead

We provide:
Our final logo (PNG)
Three design references (Inspiration1, Inspiration2, Inspiration3) to spark ideas — but you are absolutely free to propose your own creative solutions based on these concepts.

What we want:
A clean, modern, and trustworthy style
A subtle but creative watermark or graphic detail on the letterhead (not too invasive)

The same visual "family feeling" across business card, envelope, and letterhead: designs must be different but clearly connected

Strong readability for all text and contact details

Use our brand colors (Navy Blue, Green, Orange/Red) in a smart, non-overloaded way

No strict limitations: we are open to creative proposals as long as they are coherent, elegant, and suitable for professional use

Technical specifications:
100% full A4 page layout (no accidental borders)

Deliver ready-to-print PDFs and vector files (AI, EPS)

Respect 5 mm safety margins

Standard sizes for A4, business card, envelope C6 with window at the right

Tone:
Modern – Clean – Elegant – Creative – Trustworthy

Target Market(s)

Professional businesses, property managers, condominium administrators, companies, clinics, and offices requiring cleaning, gardening, and pest control services. The design must convey trust, reliability, professionalism, and attention to detail.

Industry/Entity Type

Cleaning Services, Gardening Services, Pest Control Services

Colors
0054AA
0677BA
7BADD7
CADEEF
E8F1F8
59FF00
82FF00
B8FF75
E3FFCB
F4FFEA
EB3D1F
EC4F4E
F09395
F8D3D4
FCEDEE

Requirements
Must have
• Cohesive design across business card, letterhead, and envelope Clean, modern, professional look Use of brand colors: Navy Blue (main), Green, Orange/Red accents Letterhead must include a subtle watermark without interfering with text Envelope must be with a transparent window for recipient address visibility High readability of all text and contact details Proper alignment, no unnecessary margins (full A4 layout)
Nice to have
• Creative but discreet use of the checkmark from the logo as part of the background or watermark Slight variation or accent of color tones while respecting brand identity A clean visual accent that gives a sense of movement or dynamic professionalism (without being distracting) Icons for email, phone, and website on the business card (if stylistically appropriate)
Should not have
• Overuse of colors or rainbow effects Heavy backgrounds or complex textures that interfere with readability Fonts that are too playful, comic-style, or non-professional Overcrowded layouts — the design must feel clean and spacious Watermarks that are too strong or central (they must be subtle and marginal)

```html
<!DOCTYPE html>
<html lang="en">
<head>
<meta charset="utf-8">
<title>MERIDA CARE – Corporate Identity Pack</title>
<link rel="stylesheet" href="https://fonts.googleapis.com/css2?family=Roboto:wght@400;500;700&display=swap">
<style>
:root{
  --navy:#0b0a78;
  --green:#6cc72c;
  --orange:#f26a1b;
  --ink:#3a3a44;
  --paper:#f6f5f6;
  --white:#ffffff;
  --stage:#3b3e41;
  --mark-navy:rgba(11,10,120,.10);
  --mark-green:rgba(108,199,44,.12);
  --mark-orange:rgba(242,106,27,.10);
}
*{box-sizing:border-box;margin:0;padding:0}
html,body{width:1200px;height:597px;overflow:hidden;background:var(--stage);font-family:"Roboto",Arial,sans-serif;color:var(--ink)}
.canvas{position:relative;width:1200px;height:597px}
.abs{position:absolute}

/* brand name lockup */
.brand{display:flex;align-items:center;gap:4px;font-weight:700;color:var(--navy);letter-spacing:.02em;white-space:nowrap}
.brand-square{display:inline-block;background:var(--green)}

/* soft watermark field */
.watermark{position:absolute;background:linear-gradient(160deg,var(--mark-navy) 0%,var(--mark-navy) 35%,var(--mark-green) 70%,var(--mark-orange) 100%)}

/* bottom band */
.band{position:absolute;left:0;right:0;bottom:0}
.band-green{position:absolute;left:0;bottom:0;background:var(--green)}
.band-navy{position:absolute;right:0;bottom:0;background:var(--navy);color:var(--white);font-weight:500;display:flex;align-items:center;justify-content:flex-end;clip-path:polygon(6% 0,100% 0,100% 100%,0 100%)}

.contact{list-style:none}
.contact li{display:flex;align-items:center;gap:3px;white-space:nowrap}
.contact svg{flex:none}

/* business card front */
.card-front{left:44px;top:120px;width:256px;height:146px;background:var(--white);border-radius:8px;overflow:hidden}
.card-front .brand{position:absolute;left:24px;top:64px;font-size:11px}
.card-front .divider{position:absolute;left:125px;top:26px;width:1px;height:90px;background:#c9c9d0}
.card-front .person{position:absolute;left:135px;top:27px}
.person-name{font-size:9.5px;font-weight:700;color:var(--navy);letter-spacing:.02em}
.person-role{font-size:5.5px;color:var(--green)}
.card-front .address{position:absolute;left:135px;top:53px;font-size:5.6px;line-height:7.4px}
.card-front .contact{position:absolute;left:132px;top:87px;font-size:5.6px;line-height:7.4px}

/* business card back */
.card-back{left:39px;top:322px;width:261px;height:150px;background:var(--navy);border-radius:8px}
.card-back .brand{position:absolute;left:0;right:0;top:48px;justify-content:center;color:var(--white);font-size:17px;gap:6px}
.card-back .url{position:absolute;left:0;right:0;top:128px;text-align:center;color:var(--white);font-size:6px;font-weight:500}

/* letterhead */
.letterhead{left:327px;top:52px;width:358px;height:505px;background:var(--paper);overflow:hidden}
.letterhead .watermark{left:53px;top:127px;width:254px;height:250px}
.letterhead .brand{position:absolute;left:23px;top:44px;font-size:11px}
.letterhead .head-address{position:absolute;right:105px;top:34px;text-align:right;font-size:5.4px;line-height:7.3px}
.letterhead .head-divider{position:absolute;left:257px;top:33px;width:1px;height:30px;background:#b9b9c2}
.letterhead .contact{position:absolute;left:262px;top:34px;font-size:5.4px;line-height:7.3px}
.salutation{position:absolute;left:36px;top:123px;font-size:9.5px;color:#4a4a55}
.body-copy{position:absolute;left:36px;top:154px;width:288px;font-size:4.9px;line-height:8.6px;color:#5a5a66;text-align:justify}
.body-copy p{margin-bottom:8.6px}
.closing{position:absolute;left:36px;top:343px;font-size:5.4px;color:#5a5a66}
.signature{position:absolute;left:33px;top:357px}
.signer{position:absolute;left:37px;top:383px;font-size:8px;color:#4a4a55}
.signer small{display:block;font-size:5.8px;margin-top:2px}

/* envelope back */
.envelope-back{left:746px;top:169px;width:402px;height:183px;background:#f7f6f7}
.envelope-back svg.flap{position:absolute;left:0;top:0}
.envelope-back .brand{position:absolute;left:0;right:0;top:24px;justify-content:center;color:var(--white);font-size:14px;gap:6px}

/* envelope front */
.envelope-front{left:715px;top:266px;width:404px;height:184px;background:var(--paper);box-shadow:0 2px 6px rgba(0,0,0,.25);overflow:hidden}
.envelope-front .watermark{left:221px;top:8px;width:174px;height:162px}
.envelope-front .brand{position:absolute;left:26px;top:28px;font-size:14px}
.envelope-front .window{position:absolute;left:212px;top:67px;width:157px;height:63px;border-radius:4px;background:rgba(255,255,255,.55);box-shadow:0 1px 3px rgba(0,0,0,.18)}
.envelope-front .address{position:absolute;left:23px;top:105px;font-size:5.6px;line-height:7.4px}
.envelope-front .contact{position:absolute;left:22px;top:142px;font-size:5.6px;line-height:7.4px}
</style>
</head>
<body>
<div class="canvas">

  <section class="abs card-front" aria-label="Business card front">
    <div class="brand"><span class="brand-square" style="width:10px;height:10px"></span>MERIDA CARE</div>
    <div class="divider"></div>
    <div class="person">
      <div class="person-name">MARCO VERDI</div>
      <div class="person-role">President</div>
    </div>
    <div class="address">Via dei Tigli 24 - Lindenweg 24<br>I-39100 Castelnuovo (Bz)<br>REA-VWV Nr. Bz 310752<br>P.I.-MwSt. 04418270553</div>
    <ul class="contact">
      <li><svg width="7" height="6" viewBox="0 0 10 10"><path d="M2 1l2 2-1 1.5c.8 1.5 1.7 2.4 3 3L7.5 6l2 2-1.5 1.5C4.5 9 1 5.5.5 2z" fill="var(--orange)"/></svg>+39 340 555 0182</li>
      <li><svg width="7" height="6" viewBox="0 0 10 8"><rect width="10" height="8" fill="var(--orange)"/><path d="M0 0l5 4 5-4" fill="none" stroke="#fff" stroke-width="1"/></svg>office@merida-care.srl</li>
      <li><svg width="7" height="5" viewBox="0 0 10 6"><rect x=".5" y=".5" width="9" height="5" rx="2.5" fill="none" stroke="var(--navy)"/></svg>info.meridacare@pec.it</li>
      <li><svg width="7" height="5" viewBox="0 0 10 6"><rect x=".5" y=".5" width="9" height="5" rx="2.5" fill="none" stroke="var(--navy)"/></svg>Q7TLNR4</li>
    </ul>
    <div class="band">
      <div class="band-green" style="width:100%;height:4px"></div>
      <div class="band-navy" style="width:98px;height:11px;padding-right:16px;font-size:5.6px">www.merida-care.srl</div>
    </div>
  </section>

  <section class="abs card-back" aria-label="Business card back">
    <div class="brand"><span class="brand-square" style="width:16px;height:16px"></span>MERIDA CARE</div>
    <div class="url">www.merida-care.srl</div>
  </section>

  <section class="abs letterhead" aria-label="A4 letterhead">
    <div class="watermark" role="img" aria-label="Faint brand watermark in navy, green and orange tints"></div>
    <div class="brand"><span class="brand-square" style="width:10px;height:10px"></span>MERIDA CARE</div>
    <div class="head-address">Via dei Tigli 24 - Lindenweg 24<br>I-39100 Castelnuovo (Bz)<br>REA-VWV Nr. Bz 310752<br>P.I.-MwSt. 04418270553</div>
    <div class="head-divider"></div>
    <ul class="contact">
      <li><svg width="6" height="6" viewBox="0 0 10 10"><path d="M2 1l2 2-1 1.5c.8 1.5 1.7 2.4 3 3L7.5 6l2 2-1.5 1.5C4.5 9 1 5.5.5 2z" fill="var(--orange)"/></svg>+39 340 555 0182</li>
      <li><svg width="6" height="5" viewBox="0 0 10 8"><rect width="10" height="8" fill="var(--orange)"/><path d="M0 0l5 4 5-4" fill="none" stroke="#fff" stroke-width="1"/></svg>office@merida-care.srl</li>
      <li><svg width="7" height="5" viewBox="0 0 10 6"><rect x=".5" y=".5" width="9" height="5" rx="2.5" fill="none" stroke="var(--navy)"/></svg>info.meridacare@pec.it</li>
      <li><svg width="7" height="5" viewBox="0 0 10 6"><rect x=".5" y=".5" width="9" height="5" rx="2.5" fill="none" stroke="var(--navy)"/></svg>Q7TLNR4</li>
    </ul>

    <div class="salutation">Dear Mr. Rossi,</div>
    <div class="body-copy">
      <p>Lorem ipsum dolor sit amet, consectetur adipiscing elit. Donec orci purus, luctus vitae dignissim eu, iaculis sed purus. Vivamus faucibus, ipsum nec aliquet viverra, leo mauris condimentum ligula, sit amet sagittis enim ligula quis arcu. Nam egestas tortor id nisi porttitor mattis. In tortor ante, ultricies in suscipit a, tempus non massa. Vivamus et auctor mi. Fusce vel massa nulla. Phasellus nec eros mauris, et scelerisque orci.</p>
      <p>Donec malesuada orci vitae nulla accumsan porta a id massa. Quisque accumsan iaculis magna sit amet fringilla. Maecenas consequat, magna eget tincidunt semper, odio nibh rutrum mi, id feugiat ante nisi eu risus. Vestibulum nunc orci, rhoncus a placerat in, ultricies in mi. Cras mattis varius eros, vel fringilla nisi suscipit eget. Quisque scelerisque sagittis nulla at porttitor.</p>
      <p>Sed id augue vitae urna euismod commodo aliquet a quam. Pellentesque arcu velit, cursus et malesuada ut, consequat et diam. Nullam erat sem, rhoncus id ullamcorper vitae, rhoncus et arcu. In ultricies ultricies nulla, ut rutrum nisi iaculis at. Donec eu magna a metus ornare faucibus. Fusce aliquet faucibus ultricies. Morbi semper, est id tincidunt gravida, sem arcu adipiscing lacus, ac bibendum nulla leo eu purus. Quisque nec diam sed risus consectetur accumsan quis quis nibh. Vestibulum id purus lorem.</p>
      <p>It is a long established fact that a reader will be distracted by the readable content of a page when looking at its layout. The point of using Lorem Ipsum is that it has a more-or-less normal distribution of letters, as opposed to using 'Content here, content here', making it look like readable English. Many desktop publishing packages</p>
    </div>
    <div class="closing">Sincerely,</div>
    <svg class="signature" width="48" height="20" viewBox="0 0 48 20" aria-hidden="true">
      <path d="M2 9c10-2 20-3 30-1 4 1 9 2 14 1M22 3c3 2 4 7 2 13M26 8c3 1 5 3 4 5" fill="none" stroke="#222" stroke-width=".8"/>
    </svg>
    <div class="signer">Marco Verdi<small>CEO/ Founder</small></div>

    <div class="band">
      <div class="band-green" style="width:60%;height:7px"></div>
      <div class="band-navy" style="width:162px;height:14px;padding-right:22px;font-size:6px">www.merida-care.srl</div>
    </div>
  </section>

  <section class="abs envelope-back" aria-label="Envelope back">
    <svg class="flap" width="402" height="68" viewBox="0 0 402 68" aria-hidden="true">
      <path d="M0 0H402L394 40Q390 67 362 67H40Q12 67 8 40Z" fill="var(--navy)"/>
    </svg>
    <div class="brand"><span class="brand-square" style="width:14px;height:14px"></span>MERIDA CARE</div>
  </section>

  <section class="abs envelope-front" aria-label="Envelope front">
    <div class="watermark" role="img" aria-label="Faint brand watermark in navy, green and orange tints"></div>
    <div class="brand"><span class="brand-square" style="width:14px;height:14px"></span>MERIDA CARE</div>
    <div class="window"></div>
    <div class="address">Via dei Tigli 24 - Lindenweg 24<br>I-39100 Castelnuovo (Bz)<br>REA-VWV Nr. Bz 310752<br>P.I.-MwSt. 04418270553</div>
    <ul class="contact">
      <li><svg width="7" height="6" viewBox="0 0 10 10"><path d="M2 1l2 2-1 1.5c.8 1.5 1.7 2.4 3 3L7.5 6l2 2-1.5 1.5C4.5 9 1 5.5.5 2z" fill="var(--orange)"/></svg>+39 340 555 0182</li>
      <li><svg width="7" height="6" viewBox="0 0 10 8"><rect width="10" height="8" fill="var(--orange)"/><path d="M0 0l5 4 5-4" fill="none" stroke="#fff" stroke-width="1"/></svg>office@merida-care.srl</li>
      <li><svg width="7" height="5" viewBox="0 0 10 6"><rect x=".5" y=".5" width="9" height="5" rx="2.5" fill="none" stroke="var(--navy)"/></svg>info.meridacare@pec.it</li>
      <li><svg width="7" height="5" viewBox="0 0 10 6"><rect x=".5" y=".5" width="9" height="5" rx="2.5" fill="none" stroke="var(--navy)"/></svg>Q7TLNR4</li>
    </ul>
    <div class="band">
      <div class="band-green" style="width:100%;height:6px"></div>
      <div class="band-navy" style="width:186px;height:14px;padding-right:22px;font-size:6px">www.merida-care.srl</div>
    </div>
  </section>

</div>
</body>
</html>
```